Business Card Design for Massage Therapist

*I am a qualified massage therapist & require a business card for my new business 'Tidal Bodywork & Wellness'.
*Contact details I'd like included on the card are: Hester Pradley, Mobile: 0481539260, Email: tidalbw@quillpost.com
*It is a massage business dedicated to providing quality therapeutic massage treatments, that will later incorporate natural therapies.
* Styles Include: Swedish, Relaxation, Pregnancy, Deep Tissue & Sports Massage
*I offer the styles of massage as listed above & a mobile service that allows clients to book a massage in the comfort of their own home.
*I'd like my logo to be fairly simple, streamlined, modern & reflect what my business services are - one people will easily remember.
*I'd like the colors to represent & emit a sense of calm, be fresh, welcoming, natural colors that appeal to a wide range of people.
*Colors I'd like to see are: pale blue, aqua & greens.

Target Market(s)

Both Male & Female, aged 20 to 65, singles, couples, parents, business people who are interested in their health, fitness & general wellbeing and maintenance. Located in the Fernvale area and surrounding suburbs of Melbourne.

Industry/Entity Type

Massage

Requirements
Must have
• Fonts used in logos should be owned by the designer.
Should not have
• I don't want the design to have someone being massaged in it (pictures/photos) or have it look too clinical & sterile.

```html
<!DOCTYPE html>
<html lang="en">
<head>
<meta charset="utf-8">
<title>Tidal Bodywork &amp; Wellness – Business Card</title>
<link rel="stylesheet" href="https://fonts.googleapis.com/css2?family=Open+Sans:wght@400;600;700&display=swap">
<style>
  :root {
    --backdrop: #8d8d8d;
    --card-white: #ffffff;
    --sky: #a3d9f5;
    --sea-green: #1aae87;
    --mint: #8fd2b4;
    --ink: #141414;
    --ink-soft: #222;
  }
  html, body {
    margin: 0;
    width: 1200px;
    height: 900px;
    overflow: hidden;
    background: var(--backdrop);
    font-family: "Open Sans", Arial, sans-serif;
  }
  .card {
    position: absolute;
    left: 110px;
    top: 170px;
    width: 980px;
    height: 560px;
    background: var(--card-white);
    overflow: hidden;
    box-shadow: 0 10px 30px rgba(0,0,0,0.25);
  }
  .card-waves {
    position: absolute;
    inset: 0;
    width: 980px;
    height: 560px;
  }
  .brand {
    position: absolute;
    right: 60px;
    top: 70px;
    display: flex;
    align-items: center;
    gap: 18px;
  }
  .brand-mark {
    width: 52px;
    height: 52px;
    background: var(--sea-green);
  }
  .brand-name {
    font-size: 40px;
    font-weight: 600;
    color: var(--ink);
    letter-spacing: 0.2px;
  }
  .therapist {
    position: absolute;
    left: 60px;
    top: 370px;
    color: var(--ink);
  }
  .therapist-name {
    margin: 0;
    font-size: 32px;
    font-weight: 700;
    line-height: 1.15;
  }
  .therapist-role {
    margin: 2px 0 0;
    font-size: 21px;
    color: var(--ink-soft);
  }
  .contact-list {
    list-style: none;
    margin: 26px 0 0;
    padding: 0;
  }
  .contact-item {
    display: flex;
    align-items: center;
    gap: 12px;
    font-size: 21px;
    margin-bottom: 10px;
    color: var(--ink-soft);
  }
  .contact-icon {
    width: 22px;
    height: 22px;
    flex: none;
  }
  .services {
    position: absolute;
    left: 560px;
    top: 380px;
    margin: 0;
    font-size: 21px;
    line-height: 1.45;
    color: var(--ink-soft);
  }
</style>
</head>
<body>
  <main class="card">
    <svg class="card-waves" viewBox="0 0 980 560" aria-hidden="true">
      <path d="M0,205 C230,370 640,340 980,165 L980,560 L0,560 Z" fill="var(--sea-green)"/>
      <path d="M0,250 C260,390 660,360 980,180 L980,560 L0,560 Z" fill="var(--sky)"/>
    </svg>

    <div class="brand">
      <span class="brand-mark"></span>
      <span class="brand-name">Tidal Bodywork &amp; Wellness</span>
    </div>

    <section class="therapist">
      <h1 class="therapist-name">Hester Pradley</h1>
      <p class="therapist-role">Massage Therapist</p>
      <ul class="contact-list">
        <li class="contact-item">
          <svg class="contact-icon" viewBox="0 0 22 22" aria-hidden="true">
            <rect width="22" height="22" rx="3" fill="var(--sea-green)"/>
            <rect x="7" y="4" width="8" height="14" rx="1.5" fill="none" stroke="#fff" stroke-width="1.6"/>
            <circle cx="11" cy="15.5" r="0.9" fill="#fff"/>
          </svg>
          0481 539 260
        </li>
        <li class="contact-item">
          <svg class="contact-icon" viewBox="0 0 22 22" aria-hidden="true">
            <rect width="22" height="22" rx="3" fill="var(--sea-green)"/>
            <rect x="4" y="6.5" width="14" height="9.5" fill="none" stroke="#fff" stroke-width="1.5"/>
            <path d="M4,6.5 L11,12 L18,6.5" fill="none" stroke="#fff" stroke-width="1.5"/>
          </svg>
          tidalbw@quillpost.com
        </li>
      </ul>
    </section>

    <p class="services">Swedish, Relaxation, Pregnancy.<br>Deep Tissue &amp; Sports Massage</p>
  </main>
</body>
</html>
```